Professional "Save the Date" Design

We are looking for a professional designer to create a clean, modern, and eye-catching "Save the Date" invitation that will be sent to a select group of physicians participating in our TAVREN Study.
Key Requirements:
The LORAM logo should be clearly featured and lead the branding.
The OBEN GRAFT TX logo should also appear but be subordinate to the LORAM logo.
The design should be professional, modern, and easy to read — no busy or cluttered layouts.
The final product will be used in email communications (PDF or image format).
The project is time-sensitive: we would like to have the final version completed by end of day tomorrow.
Deliverables:
Final design in high-resolution PDF and image formats (PNG or JPG).
Editable file (Adobe Illustrator, InDesign, or similar) if possible.
Details:
Monday, June 23, 2025
4:30-5:15pm EST
Name of Call: TAVREN Investigator Call
Location: Virtual (PELLO Call)
Please include this blurb as well: "Join us for a TAVREN Study Investigator Call as we welcome all participating sites and provide key information to support a successful launch. We’ll cover points of contact, upcoming study-related events, and next steps as we begin site activation."
Physicians
Medical Device

```html
<!DOCTYPE html>
<html lang="en">
<head>
<meta charset="UTF-8">
<title>Save the Date – TAVREN Investigator Call</title>
<link rel="stylesheet" href="https://fonts.googleapis.com/css2?family=Alegreya:wght@400;500&family=Courier+Prime&display=swap">
<style>
  :root {
    --paper: #eef0ee;
    --wash-light: #dfe4df;
    --wash-mid: #c4cdc4;
    --wash-deep: #8f9c90;
    --heading: #6d7b6d;
    --body: #2a2e2c;
    --detail: #5f7a5d;
    --brand-primary: #8cc63f;
    --brand-secondary: #8a1f6e;
  }
  * { margin: 0; padding: 0; box-sizing: border-box; }
  html, body { width: 1200px; height: 800px; overflow: hidden; background: var(--paper); }
  .invite {
    position: relative;
    width: 1200px;
    height: 800px;
    background: var(--paper);
    overflow: hidden;
    font-family: "Alegreya", Georgia, serif;
  }
  .invite__wash {
    position: absolute;
    inset: 0;
    background:
      radial-gradient(ellipse 300px 200px at 1020px 80px, var(--wash-mid) 0%, transparent 70%),
      radial-gradient(ellipse 240px 320px at 1190px 330px, var(--wash-deep) 0%, transparent 70%),
      radial-gradient(ellipse 280px 220px at 960px 580px, var(--wash-mid) 0%, transparent 72%),
      radial-gradient(ellipse 360px 240px at 1060px 790px, var(--wash-deep) 0%, transparent 70%),
      radial-gradient(ellipse 300px 260px at 640px 740px, var(--wash-light) 0%, transparent 70%),
      radial-gradient(ellipse 320px 200px at 720px 60px, var(--wash-light) 0%, transparent 70%);
    opacity: 0.85;
  }
  .invite__title {
    position: absolute;
    left: 83px;
    top: 112px;
    font-weight: 500;
    font-size: 30px;
    letter-spacing: 0.2em;
    color: var(--heading);
    text-transform: uppercase;
    white-space: nowrap;
  }
  .invite__blurb {
    position: absolute;
    left: 83px;
    top: 236px;
    width: 760px;
    font-size: 26px;
    line-height: 40px;
    color: var(--body);
  }
  .event-details {
    position: absolute;
    left: 83px;
    top: 432px;
    width: 460px;
    list-style: none;
    font-family: "Courier Prime", "Courier New", monospace;
    font-size: 25px;
    line-height: 30px;
    letter-spacing: 0.1em;
    color: var(--detail);
    text-transform: uppercase;
    text-align: justify;
  }
  .event-details li { text-align-last: left; }
  .brand {
    position: absolute;
    font-family: "Alegreya", Georgia, serif;
    font-weight: 500;
    line-height: 1;
    white-space: nowrap;
  }
  .brand--primary {
    left: 940px;
    top: 292px;
    font-size: 58px;
    color: var(--brand-primary);
  }
  .brand--secondary {
    left: 898px;
    top: 430px;
    font-size: 34px;
    letter-spacing: 0.02em;
    color: var(--brand-secondary);
  }
</style>
</head>
<body>
  <main class="invite">
    <div class="invite__wash" role="img" aria-label="Soft sage and grey watercolour leaf shapes washing across the right side"></div>

    <h1 class="invite__title">Save the Date</h1>
    <p class="invite__blurb">Join us for a TAVREN Study Investigator Call as we welcome all participating sites and provide key information to support a successful launch. We’ll cover points of contact, upcoming study-related events, and next steps as we begin site activation.</p>

    <ul class="event-details">
      <li>Monday, June 23, 2025</li>
      <li>4:30-5:15pm EST</li>
      <li>Name of Call: TAVREN Investigator Call</li>
      <li>Location: Virtual (PELLO Call)</li>
    </ul>

    <div class="brand brand--primary">LORAM</div>
    <div class="brand brand--secondary">OBEN GRAFT TX</div>
  </main>
</body>
</html>
```